Harborline Capital Inc. Investor Presentation

We would like a PowerPoint presentation to attract prospective investors. It needs to look extremely professional since we are a financial lending institution, and seeking capital investors. We specialize in Private Lending with Mortgage Backed Securities, both Residential and Commercial properties.

```html
<!DOCTYPE html>
<html lang="en">
<head>
<meta charset="utf-8">
<title>Harborline Capital Inc. — Investor Presentation</title>
<link href="https://fonts.googleapis.com/css2?family=Cormorant+Garamond:wght@600;700&family=Roboto:wght@400;700&display=swap" rel="stylesheet">
<style>
:root{
  --page:#eeebe7;
  --white:#ffffff;
  --navy:#1b2559;
  --blue:#1565a8;
  --ink:#333a44;
  --black:#111111;
}
*{box-sizing:border-box;margin:0;padding:0}
html,body{width:1200px;height:4098px;overflow:hidden;background:var(--page)}
body{position:relative;font-family:'Roboto',Arial,sans-serif;color:var(--ink)}
.slide{position:absolute;left:51px;width:1098px;height:618px;background:var(--white);overflow:hidden;box-shadow:0 1px 3px rgba(0,0,0,.08)}
.abs{position:absolute}
.serif{font-family:'Cormorant Garamond',Georgia,serif}
.heading{position:absolute;left:0;width:100%;text-align:center;font-family:'Cormorant Garamond',Georgia,serif;font-weight:700;font-size:38px;color:var(--navy);letter-spacing:.5px;line-height:1}
.logo{position:absolute;font-family:'Cormorant Garamond',Georgia,serif;font-weight:600;color:var(--navy);text-align:center;line-height:1}
.logo .name{font-size:26px;letter-spacing:.5px}
.logo .sub{font-size:13px;letter-spacing:2px;margin-top:3px}
.logo-top{right:20px;top:22px;width:170px}
.logo-box{background:var(--white);display:flex;flex-direction:column;align-items:center;justify-content:center}
.body-text{font-size:10.5px;line-height:20px;color:var(--ink);text-align:justify}
.center-text{position:absolute;left:135px;width:828px;text-align:center;font-size:10.5px;line-height:21px;color:var(--ink)}
.corner{position:absolute;right:0;bottom:0;width:58px;height:55px}
.photo{position:absolute}
/* services */
.service{position:absolute;top:189px;width:264px}
.service .photo{left:0;top:0;width:264px;height:191px}
.service .badge{position:absolute;left:99px;top:155px;width:66px;height:66px;border-radius:50%;background:var(--blue);border:3px solid var(--white)}
.service h3{position:absolute;top:234px;width:100%;text-align:center;font-size:20px;font-weight:700;color:var(--black)}
.service p{position:absolute;top:266px;width:100%;font-size:9.5px;line-height:17px;text-align:center;color:var(--ink)}
/* solution */
.band{position:absolute;left:0;top:145px;width:1026px;height:328px;background:var(--blue);border-radius:0 170px 170px 0}
.sol{position:absolute;top:190px;width:210px;text-align:center;color:var(--white)}
.sol svg{display:block;margin:0 auto}
.sol h3{margin-top:16px;font-size:16px;font-weight:700}
.sol p{margin-top:18px;font-size:8.8px;line-height:17.5px;text-align:justify;text-align-last:center;opacity:.95}
.divider{position:absolute;top:256px;width:1px;height:127px;background:rgba(255,255,255,.7)}
/* process */
.step{position:absolute;width:150px;text-align:center}
.step h4{font-family:'Cormorant Garamond',Georgia,serif;font-weight:700;font-size:15px;color:var(--navy)}
.step p{margin-top:6px;font-size:10.5px;line-height:20px;color:var(--ink)}
.year{position:absolute;width:122px;height:122px;border-radius:50%;background:var(--blue);color:var(--white);display:flex;align-items:center;justify-content:center;font-family:'Cormorant Garamond',Georgia,serif;font-weight:700;font-size:24px}
/* contact */
.contact{position:absolute;top:504px;left:0;width:1098px;height:114px;background:var(--blue)}
.contact-item{position:absolute;top:28px;color:var(--white)}
.contact-item h5{font-family:'Cormorant Garamond',Georgia,serif;font-weight:600;font-size:22px;line-height:1}
.contact-item p{margin-top:10px;font-family:'Cormorant Garamond',Georgia,serif;font-size:14px;line-height:19px}
.contact-item svg{position:absolute;top:2px}
</style>
</head>
<body>

<!-- Cover -->
<section class="slide" style="top:40px">
  <div class="photo" role="img" aria-label="City skyline in blue tones with a businessman holding an umbrella reflected in water" style="inset:0;background:linear-gradient(180deg,#2c4f8f 0%,#6f8fc3 35%,#b9c9e3 60%,#8aa3cb 80%,#4f6fa8 100%)"></div>
  <div class="abs" style="left:99px;top:449px;width:200px;height:168px;background:var(--blue)"></div>
  <h1 class="abs serif" style="left:188px;top:486px;width:720px;font-size:28px;line-height:34px;font-weight:700;color:var(--white);text-transform:uppercase;letter-spacing:.3px">Harborline Capital is a leading private investor and business accelerator that leverages the experience</h1>
  <div class="logo logo-box" style="left:835px;top:3px;width:202px;height:112px">
    <div class="name">HARBORLINE</div>
    <div class="sub">CAPITAL INC.</div>
  </div>
</section>

<!-- About -->
<section class="slide" style="top:715px">
  <div class="photo" role="img" aria-label="Three colleagues meeting at a table in a bright office" style="left:30px;top:40px;width:438px;height:390px;border:1px solid #ccc;background:linear-gradient(135deg,#d9d4cc 0%,#b7a898 40%,#6b6a72 70%,#ece8e2 100%)"></div>
  <div class="abs serif" style="left:30px;top:452px;width:438px;height:126px;background:var(--blue);color:var(--white);display:flex;align-items:center;justify-content:center;text-align:center;padding:0 24px;font-size:17px;line-height:26px;font-weight:600">Lorem ipsum dolor sit amet, consectetur adipiscing elit, sed do eiusmod tempor incididunt ut labore et dolore magna aliqua.</div>
  <div class="logo logo-top"><div class="name">HARBORLINE</div><div class="sub">CAPITAL INC.</div></div>
  <h2 class="abs serif" style="left:525px;top:126px;font-size:36px;font-weight:700;color:var(--navy);line-height:1">ABOUT US</h2>
  <p class="abs body-text" style="left:519px;top:182px;width:506px">Lorem ipsum dolor sit amet, consectetur adipiscing elit, sed do eiusmod tempor incididunt ut labore et dolore magna aliqua. Ut enim ad minim veniam, quis nostrud exercitation ullamco laboris nisi ut aliquip ex ea commodo consequat. Duis aute irure dolor in reprehenderit in voluptate velit esse cillum dolore eu fugiat nulla pariatur. Excepteur sint occaecat cupidatat non proident, sunt in culpa qui officia deserunt mollit anim id est laborum.</p>
  <p class="abs body-text" style="left:519px;top:302px;width:506px">Sed ut perspiciatis unde omnis iste natus error sit voluptatem accusantium doloremque laudantium, totam rem aperiam, eaque ipsa quae ab illo inventore veritatis et quasi architecto beatae vitae dicta sunt explicabo. Nemo enim ipsam voluptatem quia voluptas sit aspernatur aut odit aut fugit, sed quia consequuntur magni dolores eos qui ratione voluptatem sequi nesciunt. Neque porro quisquam est, qui dolorem ipsum quia dolor sit amet, consectetur, adipisci velit, sed quia non numquam eius modi tempora incidunt ut labore et dolore magnam aliquam quaerat voluptatem. Ut enim ad minima veniam, quis nostrum exercitationem ullam corporis suscipit laboriosam, nisi ut aliquid ex ea commodi consequatur? Quis autem vel eum iure reprehenderit qui in ea voluptate velit esse quam nihil molestiae consequatur, vel illum qui dolorem eum fugiat quo voluptas nulla pariatur</p>
  <svg class="corner" viewBox="0 0 58 55"><polygon points="58,0 58,55 0,55" fill="var(--black)"/><polygon points="58,12 58,55 13,55" fill="var(--blue)"/><text x="47" y="48" font-size="8" fill="#fff" font-family="Roboto,sans-serif" text-anchor="middle">02</text></svg>
</section>

<!-- Services -->
<section class="slide" style="top:1391px">
  <div class="logo logo-top"><div class="name">HARBORLINE</div><div class="sub">CAPITAL INC.</div></div>
  <h2 class="heading" style="top:63px">OUR SERVICES</h2>
  <p class="center-text" style="top:117px">Lorem ipsum dolor sit amet, consectetur adipiscing elit, sed do eiusmod tempor incididunt ut labore et dolore magna aliqua. Ut enim ad minim veniam, quis nostrud exercitation ullamco laboris nisi ut aliquip ex ea commodo consequat. Duis aute irure dolor in reprehenderit in voluptate velit esse</p>

  <div class="service" style="left:107px">
    <div class="photo" role="img" aria-label="Hands reviewing documents at a desk" style="background:linear-gradient(135deg,#8a7a6a,#d9d6d0 60%,#f2f1ee)"></div>
    <div class="badge"><svg viewBox="0 0 60 60" width="60" height="60"><g fill="none" stroke="#fff" stroke-width="2"><rect x="20" y="34" width="4" height="8"/><rect x="28" y="29" width="4" height="13"/><rect x="36" y="24" width="4" height="18"/><path d="M18 30l8-7 6 4 10-9"/></g></svg></div>
    <h3>Perform</h3>
    <p>Harborline Capital is a leading private investor and business accelerator that leverages the experience, insights, and resources of its founder, Mr. Daniel R. Okafor, an accomplished entrepreneur and investor.</p>
  </div>
  <div class="service" style="left:417px">
    <div class="photo" role="img" aria-label="Advisors discussing papers with a client couple" style="background:linear-gradient(135deg,#e6e2dc,#7d6d60 50%,#c9c2b8)"></div>
    <div class="badge"><svg viewBox="0 0 60 60" width="60" height="60"><g fill="none" stroke="#fff" stroke-width="2"><circle cx="24" cy="36" r="6"/><circle cx="36" cy="36" r="6"/><path d="M24 26v-8m-3 3l3-3 3 3M36 26v-8m-3 3l3-3 3 3"/></g></svg></div>
    <h3>Protect</h3>
    <p>Harborline Capital has been investing its own capital since 1998 and has had a prestigious track record generating over $2 Billion in enterprise value across various industries including financial services, software, biotechnology</p>
  </div>
  <div class="service" style="left:726px">
    <div class="photo" role="img" aria-label="Businessman in suit working with a calculator" style="background:linear-gradient(135deg,#f1f3f5,#cfd6de 50%,#394560 80%,#e9ecef)"></div>
    <div class="badge"><svg viewBox="0 0 60 60" width="60" height="60"><g fill="none" stroke="#fff" stroke-width="2"><rect x="18" y="36" width="5" height="6"/><rect x="26" y="31" width="5" height="11"/><rect x="34" y="26" width="5" height="16"/><path d="M18 28l10-8 6 4 8-6m-4 0h4v4"/></g></svg></div>
    <h3>Prosper</h3>
    <p>The entrepreneurial heritage and innovative spirit of the firm allows it to take unconventional and creative approaches to investing, that are often contrarian and sometimes pioneering.</p>
  </div>
  <svg class="corner" viewBox="0 0 58 55"><polygon points="58,0 58,55 0,55" fill="var(--black)"/><polygon points="58,12 58,55 13,55" fill="var(--blue)"/><text x="47" y="48" font-size="8" fill="#fff" font-family="Roboto,sans-serif" text-anchor="middle">03</text></svg>
</section>

<!-- Solution -->
<section class="slide" style="top:2067px">
  <div class="logo logo-top"><div class="name">HARBORLINE</div><div class="sub">CAPITAL INC.</div></div>
  <h2 class="heading" style="top:63px">OUR SOLUTION</h2>
  <div class="band"></div>
  <div class="divider" style="left:256px"></div>
  <div class="divider" style="left:514px"></div>
  <div class="divider" style="left:770px"></div>

  <div class="sol" style="left:22px">
    <svg width="64" height="64" viewBox="0 0 64 64"><g fill="none" stroke="#fff" stroke-width="2"><rect x="8" y="24" width="44" height="24" rx="2"/><circle cx="30" cy="36" r="6"/><path d="M14 12h20l6 12M40 48h14"/></g></svg>
    <h3>Nemo enim ipsam</h3>
    <p>Lorem ipsum dolor sit amet, consectetur adipiscing elit, sed do eiusmod tempor incididunt ut labore et dolore magna aliqua. Ut enim ad minim veniam, quis nostrud exercitation ullamco laboris nisi ut aliquip ex ea commodo consequat.</p>
  </div>
  <div class="sol" style="left:280px">
    <svg width="64" height="64" viewBox="0 0 64 64"><g fill="none" stroke="#fff" stroke-width="2"><circle cx="32" cy="16" r="10"/><path d="M32 30v12m-5-5l5 5 5-5M10 48h12l8 6h22"/></g></svg>
    <h3>Nemo enim ipsam</h3>
    <p>Lorem ipsum dolor sit amet, consectetur adipiscing elit, sed do eiusmod tempor incididunt ut labore et dolore magna aliqua. Ut enim ad minim veniam, quis nostrud exercitation ullamco laboris nisi ut aliquip ex ea commodo consequat.</p>
  </div>
  <div class="sol" style="left:536px">
    <svg width="64" height="64" viewBox="0 0 64 64"><g fill="none" stroke="#fff" stroke-width="2"><circle cx="16" cy="12" r="6"/><circle cx="32" cy="12" r="6"/><circle cx="48" cy="12" r="6"/><rect x="14" y="26" width="36" height="22" rx="2"/><path d="M26 54h12M32 48v6"/></g></svg>
    <h3>Nemo enim ipsam</h3>
    <p>Lorem ipsum dolor sit amet, consectetur adipiscing elit, sed do eiusmod tempor incididunt ut labore et dolore magna aliqua. Ut enim ad minim veniam, quis nostrud exercitation ullamco laboris nisi ut aliquip ex ea commodo consequat.</p>
  </div>
  <div class="sol" style="left:794px">
    <svg width="64" height="64" viewBox="0 0 64 64"><g fill="none" stroke="#fff" stroke-width="2"><circle cx="32" cy="32" r="12"/><path d="M32 4v10M32 50v10M4 32h10M50 32h10M12 12l7 7M45 45l7 7"/></g></svg>
    <h3>Nemo enim ipsam</h3>
    <p>Lorem ipsum dolor sit amet, consectetur adipiscing elit, sed do eiusmod tempor incididunt ut labore et dolore magna aliqua. Ut enim ad minim veniam, quis nostrud exercitation ullamco laboris nisi ut aliquip ex ea commodo consequat.</p>
  </div>
  <p class="center-text" style="top:522px">Lorem ipsum dolor sit amet, consectetur adipiscing elit, sed do eiusmod tempor incididunt ut labore et dolore magna aliqua. Ut enim ad minim veniam, quis nostrud exercitation ullamco laboris nisi ut aliquip ex ea commodo consequat. Duis aute irure dolor in reprehenderit in voluptate velit esse</p>
  <svg class="corner" viewBox="0 0 58 55"><polygon points="58,0 58,55 0,55" fill="var(--black)"/><polygon points="58,12 58,55 13,55" fill="var(--blue)"/><text x="47" y="48" font-size="8" fill="#fff" font-family="Roboto,sans-serif" text-anchor="middle">04</text></svg>
</section>

<!-- Process -->
<section class="slide" style="top:2742px">
  <div class="logo logo-top"><div class="name">HARBORLINE</div><div class="sub">CAPITAL INC.</div></div>
  <h2 class="heading" style="top:65px">OUR PROCESS</h2>
  <svg class="abs" style="left:0;top:0" width="1098" height="618" viewBox="0 0 1098 618">
    <g fill="none" stroke="#8c8f96" stroke-width="1.3" stroke-dasharray="2 3">
      <path d="M107 313v74a89 89 0 0 0 178 0v-74"/>
      <path d="M460 313v74a89 89 0 0 0 178 0v-74"/>
      <path d="M815 313v74a89 89 0 0 0 178 0v-74"/>
      <path d="M283 313v-76a89 89 0 0 1 178 0v76"/>
      <path d="M637 313v-76a89 89 0 0 1 178 0v76"/>
    </g>
  </svg>
  <div class="year" style="left:135px;top:326px">2000</div>
  <div class="year" style="left:311px;top:176px">2005</div>
  <div class="year" style="left:488px;top:326px">2010</div>
  <div class="year" style="left:665px;top:176px">2015</div>
  <div class="year" style="left:843px;top:326px">2020</div>

  <div class="step" style="left:121px;top:190px"><h4>Lorem ipsum dolor</h4><p>Lorem ipsum dolor sit amet, consectetur adipiscing elit, sed do eiusmod tempor inci didunt ut labore et dolore magna aliqua.</p></div>
  <div class="step" style="left:297px;top:311px"><h4>Lorem ipsum dolor</h4><p>Lorem ipsum dolor sit amet, consectetur adipiscing elit, sed do eiusmod tempor inci didunt ut labore et dolore magna aliqua.</p></div>
  <div class="step" style="left:474px;top:190px"><h4>Lorem ipsum dolor</h4><p>Lorem ipsum dolor sit amet, consectetur adipiscing elit, sed do eiusmod tempor inci didunt ut labore et dolore magna aliqua.</p></div>
  <div class="step" style="left:651px;top:311px"><h4>Lorem ipsum dolor</h4><p>Lorem ipsum dolor sit amet, consectetur adipiscing elit, sed do eiusmod tempor inci didunt ut labore et dolore magna aliqua.</p></div>
  <div class="step" style="left:829px;top:190px"><h4>Lorem ipsum dolor</h4><p>Lorem ipsum dolor sit amet, consectetur adipiscing elit, sed do eiusmod tempor inci didunt ut labore et dolore magna aliqua.</p></div>

  <p class="center-text" style="top:525px">Lorem ipsum dolor sit amet, consectetur adipiscing elit, sed do eiusmod tempor incididunt ut labore et dolore magna aliqua. Ut enim ad minim veniam, quis nostrud exercitation ullamco laboris nisi ut aliquip ex ea commodo consequat. Duis aute irure dolor in reprehenderit in voluptate velit esse</p>
  <svg class="corner" viewBox="0 0 58 55"><polygon points="58,0 58,55 0,55" fill="var(--black)"/><polygon points="58,12 58,55 13,55" fill="var(--blue)"/><text x="47" y="48" font-size="8" fill="#fff" font-family="Roboto,sans-serif" text-anchor="middle">05</text></svg>
</section>

<!-- Thank you -->
<section class="slide" style="top:3418px">
  <div class="photo" role="img" aria-label="Blurred café table with a laptop, coffee cup and potted plant" style="inset:0;background:linear-gradient(180deg,#3a3634 0%,#6b5a4c 35%,#8f7a66 55%,#4d4540 80%,#2a2624 100%)"></div>
  <div class="logo logo-box" style="left:479px;top:103px;width:156px;height:96px">
    <div class="name" style="font-size:22px">HARBORLINE</div>
    <div class="sub" style="font-size:11px">CAPITAL INC.</div>
  </div>
  <h2 class="abs serif" style="left:0;width:100%;top:221px;text-align:center;font-size:58px;font-weight:700;color:var(--white);line-height:1;letter-spacing:1px">THANK YOU</h2>
  <div class="contact">
    <div class="contact-item" style="left:122px;padding-left:50px">
      <svg width="20" height="26" viewBox="0 0 20 26" style="left:0"><path d="M10 1a8 8 0 0 0-8 8c0 6 8 16 8 16s8-10 8-16a8 8 0 0 0-8-8z" fill="#fff"/><circle cx="10" cy="9" r="3" fill="var(--blue)"/></svg>
      <h5>Address</h5>
      <p>123, Lorem ipsum dolor sit<br>amet, consectetur adip</p>
    </div>
    <div class="contact-item" style="left:440px;padding-left:46px">
      <svg width="24" height="24" viewBox="0 0 24 24" style="left:0"><path d="M5 2l4 0 2 5-3 2a12 12 0 0 0 7 7l2-3 5 2v4a2 2 0 0 1-2 2A18 18 0 0 1 3 4a2 2 0 0 1 2-2z" fill="#fff"/></svg>
      <h5>Phone</h5>
      <p>+1 888 888 8888</p>
    </div>
    <div class="contact-item" style="left:750px;padding-left:52px">
      <svg width="30" height="22" viewBox="0 0 30 22" style="left:0"><rect x="1" y="1" width="28" height="20" rx="2" fill="#fff"/><path d="M2 3l13 10 13-10" fill="none" stroke="var(--blue)" stroke-width="2"/></svg>
      <h5>Email Address</h5>
      <p>info@companyname.com</p>
    </div>
  </div>
</section>

</body>
</html>
```